Boutique Real Estate Brokerage Maplind Realty Website Design

Winning designer work on migrate as well through zip burrow.
We need a new website as an informational hub to aid our print and digital strategy as well as showing that we are located in Brooklyn and Florida. I have a boutique real estate brokerage and advisory firm specializing in residential leasing, multifamily sales and 1031 Exchange appropriation. This won't be a portal to search properties, it will be a place for information. I'd like space for an ebook to be downloaded and information on my probate sales and multifamily leasing marketing campaigns. I included my logo and will leave it up to the designer to come up with colors to match it. I have also attached verbiage for each page. The final design should have a modern high end look that reflects gentrifying Brooklyn as well as beautiful Florida.
Thank you!
Target Market(s)
Owners of income producing real estate and develop-able land in Brooklyn, NY and Florida.
Industry/Entity Type
Real Estate
Coding
Coded - Design and coding required
Number of Pages Required
5+ page
Colors
Designer to choose colors to be used in the design.
Requirements
Must have
- A modern elegant look
Nice to have
- pictures of brooklyn and florida
Should not have
- real estate search pages

```html
<!DOCTYPE html>
<html lang="en">
<head>
<meta charset="utf-8">
<title>Maplind Realty — Boutique Real Estate Brokerage</title>
<link rel="stylesheet" href="https://fonts.googleapis.com/css2?family=Jost:wght@400;500;600&family=Playfair+Display:ital,wght@0,400;0,700;1,400&display=swap">
<style>
:root{
  --black:#050607;
  --navy:#0b3a7e;
  --navy-deep:#0a2f6b;
  --blue:#2a95d6;
  --blue-bright:#2b9ae0;
  --ink:#1a1a1a;
  --grey:#6b6f75;
  --field:#dfe6ef;
  --white:#ffffff;
  --sans:'Jost', Helvetica, Arial, sans-serif;
  --serif:'Playfair Display', Georgia, serif;
}
*{box-sizing:border-box;margin:0;padding:0}
html,body{width:1200px;height:3255px;overflow:hidden}
body{position:relative;background:var(--white);font-family:var(--sans);color:var(--ink)}

/* top bar + nav */
.topbar{position:absolute;left:0;top:0;width:1200px;height:22px;background:var(--black);font-size:11px;color:#9aa3ad}
.topbar .email{position:absolute;left:52px;top:4px}
.topbar .email span,.topbar .phone span{color:var(--blue)}
.topbar .phone{position:absolute;left:868px;top:4px}
.topbar .social{position:absolute;left:1020px;top:6px;display:flex;gap:12px}
.topbar .social i{display:block;width:10px;height:10px;border-radius:50%;background:#4a7fb3}
.nav{position:absolute;left:0;top:22px;width:1200px;height:98px;background:var(--black)}
.brand{position:absolute;left:52px;top:34px;display:flex;align-items:center;gap:12px;color:#d7dade;font-weight:600;font-size:17px;letter-spacing:2px;text-transform:uppercase}
.brand i{display:block;width:30px;height:30px;background:#8d939a}
.nav ul{list-style:none}
.nav li{position:absolute;top:44px;font-size:11px;letter-spacing:2px;color:#e6e8ea;text-transform:uppercase;font-weight:500}
.nav li.active{color:var(--blue);border-bottom:2px solid var(--blue);padding-bottom:4px}
.btn{display:inline-block;font-family:var(--sans);font-size:11px;letter-spacing:2px;text-transform:uppercase;color:var(--white);text-align:center;font-weight:500}
.nav .cta{position:absolute;left:994px;top:39px;width:128px;height:30px;line-height:30px;background:var(--blue-bright)}

/* hero */
.hero{position:absolute;left:0;top:120px;width:1200px;height:522px;background:linear-gradient(100deg,#3a2418 0%,#6b3f2a 30%,#5a4636 55%,#8c8a6a 75%,#c8cfb0 100%)}
.hero .shade{position:absolute;inset:0;background:rgba(0,0,0,.28)}
.hero .lead{position:absolute;left:0;width:1200px;top:172px;text-align:center;color:var(--white);font-size:26px}
.hero h1{position:absolute;left:0;width:1200px;top:212px;text-align:center;color:var(--white);font-family:var(--serif);font-weight:400;font-size:38px}
.hero .ghost{position:absolute;left:528px;top:294px;width:145px;height:31px;line-height:29px;border:1px solid rgba(255,255,255,.8)}
.hero svg{position:absolute}

/* about */
.about-photo{position:absolute;left:152px;top:723px;width:360px;height:442px;background:linear-gradient(160deg,#d7dfe6 0%,#b7a48f 45%,#7b8a62 100%)}
.about-photo.small{left:382px;top:1063px;width:206px;height:207px;background:linear-gradient(180deg,#9fc3e6 0%,#c69a6e 50%,#2d4a5a 100%);box-shadow:0 10px 30px rgba(0,0,0,.2)}
.about h2{position:absolute;left:612px;top:756px;width:420px;font-family:var(--serif);font-weight:400;font-size:28px;line-height:37px;color:var(--ink)}
.about h2 b{font-weight:700}
.about .copy{position:absolute;left:688px;top:905px;width:356px;font-size:13px;line-height:20px;color:var(--grey)}
.about .copy p{margin-bottom:16px}
.about .copy strong{color:#3d4146;font-weight:500}
.btn.navy{background:var(--navy);height:31px;line-height:31px;width:128px}
.about .btn{position:absolute;left:688px;top:1166px}

/* services */
.skyline{position:absolute;left:0;top:1700px;width:1200px;height:448px;background:linear-gradient(180deg,#ffffff 0%,#eef1f4 35%,#cfd6dd 75%,#bcc5ce 100%)}
.services .eyebrow{position:absolute;left:0;width:1200px;top:1354px;text-align:center;color:var(--navy);font-size:21px}
.services h2{position:absolute;left:0;width:1200px;top:1386px;text-align:center;font-family:var(--serif);font-weight:400;font-size:30px}
.card{position:absolute;top:1467px;width:282px;text-align:center}
.card .pic{height:200px}
.card h3{margin-top:28px;color:var(--navy);font-size:18px;font-weight:600}
.card p{margin:8px auto 0;width:272px;font-size:13px;line-height:20px;color:var(--grey);height:60px}
.card .btn{margin-top:18px}
.card .btn.light{background:var(--blue-bright);height:31px;line-height:31px;width:128px}

/* testimonials */
.testimonials{position:absolute;left:0;top:2148px;width:1200px;height:439px;background:var(--blue);color:var(--white);text-align:center}
.testimonials .eyebrow{position:absolute;left:0;width:1200px;top:70px;font-size:20px}
.testimonials h2{position:absolute;left:0;width:1200px;top:104px;font-family:var(--serif);font-weight:400;font-size:30px}
.testimonials blockquote{position:absolute;left:260px;width:680px;top:166px;font-family:var(--serif);font-style:italic;font-size:16px;line-height:26px}
.testimonials .avatar{position:absolute;left:568px;top:261px;width:64px;height:64px;border-radius:50%;border:3px solid var(--white);background:linear-gradient(135deg,#f1d3a5,#7fb36a)}
.testimonials .name{position:absolute;left:0;width:1200px;top:340px;font-size:16px;font-weight:500}
.testimonials svg{position:absolute;top:282px}

/* footer */
.footer{position:absolute;left:0;top:2587px;width:1200px;height:668px;background:linear-gradient(180deg,#0a3a86 0%,#0c3f8a 45%,#1b5aa3 75%,#0b3578 100%);color:var(--white)}
.footer .book{position:absolute;left:152px;top:78px}
.footer .ebook-text{position:absolute;left:282px;top:88px;width:480px;font-size:17px;line-height:24px;font-weight:500}
.footer .ebook-btn{position:absolute;left:879px;top:89px;width:167px;height:30px;line-height:30px;background:var(--blue-bright)}
.footer .rule{position:absolute;left:78px;top:175px;width:1044px;height:1px;background:rgba(255,255,255,.25)}
.footer h4{position:absolute;top:255px;font-size:17px;font-weight:500}
.field{position:absolute;height:30px;background:var(--field);color:#6a7380;font-size:11px;padding:8px 12px}
.field.select::after{content:"";position:absolute;right:12px;top:13px;border:4px solid transparent;border-top-color:#6a7380}
.contact-info{position:absolute;left:152px;top:356px;font-size:14px;line-height:19px}
.contact-info dt{font-weight:600;font-size:15px}
.contact-info dd{margin-bottom:10px}
.footer .submit{position:absolute;left:536px;top:497px;width:126px;height:30px;line-height:30px;background:var(--blue-bright)}
.footer .copyright{position:absolute;left:152px;top:617px;font-size:13px}
.footer .copyright span{color:var(--blue-bright)}
.footer .social{position:absolute;left:894px;top:612px;display:flex;gap:16px}
.footer .social i{display:block;width:30px;height:30px;border-radius:50%;background:rgba(255,255,255,.28)}
.footer .social i.on{background:var(--blue-bright)}
</style>
</head>
<body>

<header>
  <div class="topbar">
    <div class="email"><span>Email Us:</span> info@maplindrealty.com</div>
    <div class="phone"><span>Call Us:</span> 555-014-2280</div>
    <div class="social"><i></i><i></i><i></i><i></i></div>
  </div>
  <nav class="nav">
    <div class="brand"><i></i>Maplind Realty</div>
    <ul>
      <li class="active" style="left:404px">Home</li>
      <li style="left:488px">About Us</li>
      <li style="left:592px">Services</li>
      <li style="left:692px">Property Listings</li>
      <li style="left:859px">Testimonials</li>
    </ul>
    <a class="btn cta">Contact Us</a>
  </nav>
</header>

<section class="hero" role="img" aria-label="Brooklyn brownstone street with stoops and trees">
  <div class="shade"></div>
  <p class="lead">Assisting landlords increase profits</p>
  <h1>while decreasing the stress</h1>
  <a class="btn ghost">Contact Now</a>
  <svg style="left:76px;top:226px" width="14" height="22" viewBox="0 0 14 22"><path d="M12 2 3 11l9 9" fill="none" stroke="#fff" stroke-width="3"/></svg>
  <svg style="left:1110px;top:226px" width="14" height="22" viewBox="0 0 14 22"><path d="M2 2l9 9-9 9" fill="none" stroke="#fff" stroke-width="3"/></svg>
  <svg style="left:592px;top:462px" width="16" height="10" viewBox="0 0 16 10"><path d="M2 2l6 6 6-6" fill="none" stroke="#fff" stroke-width="2"/></svg>
</section>

<section class="about">
  <div class="about-photo" role="img" aria-label="Smiling family of four outdoors"></div>
  <div class="about-photo small" role="img" aria-label="Florida apartment complex beside a lake with fountain"></div>
  <h2>Maplind Realty NYC•PB<br>is a full-service <b>real estate brokerage firm</b> with</h2>
  <div class="copy">
    <p>Offices located in Brooklyn, New York and West Palm Beach, Florida. Our firm focuses on multifamily leasing, sales and Commercial Real Estate Site Selection Advisory.</p>
    <p><strong>Our clients are private and institutional multifamily real estate investors.</strong></p>
    <p>Our team differentiates ourselves by our ability to investigate the highest and best use for real estate assets as well as our high deal closing rate.</p>
  </div>
  <a class="btn navy">More Info</a>
</section>

<section class="services">
  <div class="skyline" role="img" aria-label="Faint bridge and city skyline"></div>
  <p class="eyebrow">Our Services</p>
  <h2>How We Can Help</h2>
  <article class="card" style="left:152px">
    <div class="pic" role="img" aria-label="Bright modern apartment kitchen and dining room" style="background:linear-gradient(135deg,#e8ece9,#9fb0ac 60%,#5e6f6a)"></div>
    <h3>Multi-Family Leasing</h3>
    <p>We specialize in sourcing quality tenants for landlords with high income, good credit and no evictions ...</p>
    <a class="btn navy">More Info</a>
  </article>
  <article class="card" style="left:458px">
    <div class="pic" role="img" aria-label="Brick walk-up building with fire escapes" style="background:linear-gradient(160deg,#b9c7d6,#8a6a52 45%,#5a4232)"></div>
    <h3>Multi-Family Sales</h3>
    <p>Maplind Realty provides clients with reliable real estate research, advisory and transaction services ...</p>
    <a class="btn light">More Info</a>
  </article>
  <article class="card" style="left:764px">
    <div class="pic" role="img" aria-label="Aerial view of developable land near a river" style="background:linear-gradient(180deg,#c7d3df,#8e9a7c 45%,#5c6a4e)"></div>
    <h3>Site Selection Advisory</h3>
    <p>Our industry best Commercial Real Estate site selection services assists developers in narrow down the site ...</p>
    <a class="btn navy">More Info</a>
  </article>
</section>

<section class="testimonials">
  <p class="eyebrow">Testimonials</p>
  <h2>What Our Clients Say</h2>
  <blockquote>Contrary to popular belief, Lorem Ipsum is not simply random text. It has roots in piece of classical Latin literature from 45 BC, making it over 35 years old. Corwin Halvey, a Latin professor at Ashcombe ...</blockquote>
  <svg style="left:544px" width="8" height="12" viewBox="0 0 8 12"><path d="M6 1 2 6l4 5" fill="none" stroke="#fff" stroke-width="1.5"/></svg>
  <div class="avatar" role="img" aria-label="Client portrait"></div>
  <svg style="left:648px" width="8" height="12" viewBox="0 0 8 12"><path d="M2 1l4 5-4 5" fill="none" stroke="#fff" stroke-width="1.5"/></svg>
  <p class="name">Dara Whitlow</p>
</section>

<footer class="footer" role="img" aria-label="Coastal city skyline in deep blue tones">
  <svg class="book" width="78" height="54" viewBox="0 0 78 54"><path d="M39 8C30 3 16 3 4 6v42c12-3 26-3 35 2 9-5 23-5 35-2V6C62 3 48 3 39 8zM39 8v42" fill="none" stroke="#2b9ae0" stroke-width="4" stroke-linejoin="round"/></svg>
  <p class="ebook-text">There are many variations of passages of Lorem Ipsum available, but the majority have suffered!</p>
  <a class="btn ebook-btn">Download Ebooks</a>
  <div class="rule"></div>

  <h4 style="left:152px">Contact Us</h4>
  <div class="field select" style="left:152px;top:297px;width:250px">Florida</div>
  <dl class="contact-info">
    <dt>Maplind Realty:</dt>
    <dd>4410 Harbor Palm Blvd,<br>Westlake, FL 33411</dd>
    <dt>Call Us:</dt>
    <dd>555-014-2280</dd>
    <dt>Email:</dt>
    <dd>info@maplindrealty.com</dd>
  </dl>

  <h4 style="left:536px">Send a Message</h4>
  <div class="field" style="left:536px;top:297px;width:248px">Name</div>
  <div class="field" style="left:801px;top:297px;width:245px">Email</div>
  <div class="field" style="left:536px;top:345px;width:248px">Phone</div>
  <div class="field select" style="left:801px;top:345px;width:245px">Services</div>
  <div class="field" style="left:536px;top:393px;width:510px;height:78px">Message</div>
  <a class="btn submit">Submit</a>

  <p class="copyright">© 2019 <span>Maplind Realty</span>. All Rights Reserved.</p>
  <div class="social"><i></i><i></i><i class="on"></i><i></i></div>
</footer>

</body>
</html>
```